Business Card Design

I need a business card designed for my business.

The company name is Rowan Pellet Group

It has four brands underneath it. They are:
- RP Events
- RP Sports Tours
- RPG Management
- Bold Mosaic

I have attached all logo items, as well as our last business card.

I look forward to seeing your designs.

Industry/Entity Type

Business

Colors
eb1f27
0355a3

Requirements
Must have
• Our contact details as per the front page of our previous business card.

```html
<!DOCTYPE html>
<html lang="en">
<head>
<meta charset="utf-8">
<title>Rowan Pellet Group – Business Card</title>
<link rel="stylesheet" href="https://fonts.googleapis.com/css2?family=Open+Sans:wght@400;600;700&display=swap">
<style>
  :root {
    --brand-red: #eb1f27;
    --brand-blue: #0355a3;
    --ink: #2b2b2b;
    --card-white: #fbfbfb;
    --card-shade: #ececec;
    --stage-light: #9a9a9a;
    --stage-dark: #4a4a4a;
    --label-grey: #5c5c5c;
  }
  * { margin: 0; padding: 0; box-sizing: border-box; }
  html, body { width: 1200px; height: 900px; overflow: hidden; }
  body {
    position: relative;
    font-family: "Open Sans", Arial, sans-serif;
    background: radial-gradient(ellipse at 40% 40%, var(--stage-light), var(--stage-dark));
  }
  .card {
    position: absolute;
    width: 580px;
    height: 340px;
    border-radius: 24px;
    overflow: hidden;
    background: linear-gradient(160deg, var(--card-white) 55%, var(--card-shade));
    box-shadow: 0 18px 40px rgba(0,0,0,0.35);
  }
  .card-back { left: 550px; top: 130px; }
  .card-front { left: 70px; top: 430px; }
  .swoosh { position: absolute; inset: 0; width: 100%; height: 100%; }
  .side-label {
    position: absolute;
    font-size: 46px;
    font-weight: 600;
    color: var(--label-grey);
  }
  .label-back { left: 780px; top: 488px; }
  .label-front { left: 305px; top: 786px; }

  /* front */
  .group-mark {
    position: absolute; left: 140px; top: 44px;
    display: flex; align-items: center; gap: 14px;
  }
  .group-mark .dot {
    width: 62px; height: 62px; border-radius: 50%;
    background: var(--brand-blue);
  }
  .group-mark .name {
    font-size: 30px; font-weight: 700; color: var(--brand-blue);
    letter-spacing: -0.5px;
  }
  .holder { position: absolute; left: 90px; top: 170px; text-align: right; }
  .holder .person { font-size: 30px; font-weight: 600; color: var(--brand-red); }
  .holder .role { font-size: 17px; font-weight: 600; color: var(--ink); }
  .postal {
    position: absolute; left: 350px; top: 150px;
    font-size: 16px; line-height: 1.25; color: var(--ink);
  }
  .contacts {
    position: absolute; left: 96px; bottom: 30px;
    display: flex; align-items: center; gap: 12px;
    font-size: 12.5px; line-height: 1.45; color: var(--ink);
    font-weight: 600;
  }
  .contacts .divider { width: 1px; height: 36px; background: var(--ink); }

  /* back */
  .brand-row {
    position: absolute; left: 60px; right: 60px; top: 96px;
    display: flex; justify-content: center; align-items: center; gap: 28px;
  }
  .brand { font-size: 21px; font-weight: 700; }
  .brand-red { color: var(--brand-red); }
  .brand-blue { color: var(--brand-blue); }
  .tagline {
    position: absolute; left: 0; right: 0; top: 178px;
    text-align: center; font-size: 23px; font-weight: 600;
    line-height: 1.25; color: var(--brand-blue);
  }
  .back-web {
    position: absolute; left: 0; right: 0; bottom: 40px;
    text-align: center; font-size: 13px; font-weight: 600; color: var(--ink);
  }
</style>
</head>
<body>

<section class="card card-back" aria-label="Card back">
  <svg class="swoosh" viewBox="0 0 580 340" aria-hidden="true">
    <path d="M580 0 V58 Q555 14 470 0 Z" fill="var(--brand-red)"/>
    <path d="M580 92 Q540 18 300 0 H430 Q550 14 580 68 Z" fill="var(--brand-blue)"/>
  </svg>
  <div class="brand-row">
    <span class="brand brand-red">RP Events</span>
    <span class="brand brand-blue">RP Sports Tours</span>
    <span class="brand brand-blue">RPG Management</span>
  </div>
  <p class="tagline">Event, travel and<br>talent management</p>
  <p class="back-web">www.RowanPelletGroup.com.au</p>
</section>
<p class="side-label label-back">back</p>

<section class="card card-front" aria-label="Card front">
  <svg class="swoosh" viewBox="0 0 580 340" aria-hidden="true">
    <path d="M0 0 H120 Q40 18 0 62 Z" fill="var(--brand-red)"/>
    <path d="M0 112 Q50 28 150 0 H215 Q70 28 0 78 Z" fill="var(--brand-blue)"/>
    <path d="M580 235 V340 H455 Q545 305 580 235 Z" fill="var(--brand-red)"/>
    <path d="M580 140 Q565 285 390 340 H430 Q555 300 580 212 Z" fill="var(--brand-blue)"/>
  </svg>
  <div class="group-mark">
    <span class="dot"></span>
    <span class="name">ROWAN PELLET GROUP</span>
  </div>
  <div class="holder">
    <p class="person">Rowan Pellet</p>
    <p class="role">Principal</p>
  </div>
  <address class="postal" style="font-style:normal">
    PO Box 418<br>Harlow ACT 2690<br>Australia
  </address>
  <div class="contacts">
    <p>+61 2 6100 4831<br>+61 431 555 208</p>
    <span class="divider"></span>
    <p>Rowan@RowanPelletGroup.com.au<br>www.RowanPelletGroup.com.au</p>
  </div>
</section>
<p class="side-label label-front">front</p>

</body>
</html>
```